Private Investigation Business Card Design

I need a business card for a new private investigation company named Brisk Lens Inquiries. I perform mainly surveillance jobs, vehicle repossessions, document serves etc. The final design should aim for a professional look. The logo has a magnifying glass with stick man arms and legs and is in a running action to show the "BRISK" aspect of the name. If the colour scheme could remain the same as the website www.brisklensinquiries.example.au with silvers,blacks and a couple electric blue highlights.
Industry/Entity Type
Business
Contact Information for Business Card
Morgan Kilbride
Brisk Lens Inquiries
0438276104
PO Box 58, Fernvale NSW 2291
info@brisklensinquiries.example.au
www.brisklensinquiries.example.au
Look and feel
Each slider illustrates characteristics of the customer's brand and the style your logo design should communicate.

```html
<!DOCTYPE html>
<html lang="en">
<head>
<meta charset="utf-8">
<title>Brisk Lens Inquiries – Business Card</title>
<link href="https://fonts.googleapis.com/css2?family=Open+Sans:wght@400;700&display=swap" rel="stylesheet">
<style>
  :root {
    --backdrop: #3b3532;
    --card-black: #141414;
    --card-sheen: #3a3a3a;
    --silver: #c9c9c9;
    --silver-dark: #8e8e8e;
    --text-light: #f2f2f2;
    --text-muted: #b5b5b5;
  }
  * { margin: 0; padding: 0; box-sizing: border-box; }
  html, body {
    width: 1200px; height: 844px; overflow: hidden;
    background: var(--backdrop);
    font-family: "Open Sans", Arial, sans-serif;
  }
  .stage {
    position: relative; width: 1200px; height: 844px;
    display: flex; align-items: center; justify-content: center; gap: 60px;
  }
  .card {
    position: relative; width: 520px; height: 318px; overflow: hidden;
    background: var(--card-black);
    box-shadow: 0 12px 30px rgba(0,0,0,.45);
  }
  /* Contact side */
  .card--contact {
    background: linear-gradient(120deg, #0f0f0f 0%, #1c1c1c 55%, #2c2c2c 100%);
  }
  .edge-band {
    position: absolute; top: 0; bottom: 0; width: 26px;
    background: linear-gradient(90deg, var(--silver-dark), var(--silver), #e6e6e6);
  }
  .edge-band--left { left: 0; }
  .edge-band--right { right: 0; }
  .mascot-area {
    position: absolute; left: 40px; top: 96px; width: 170px; height: 210px;
    background: radial-gradient(ellipse at 40% 40%, #d8d8d8 0%, #9a9a9a 45%, rgba(40,40,40,0) 75%);
    opacity: .55;
  }
  .contact-block {
    position: absolute; left: 200px; right: 40px; top: 62px;
    text-align: center; color: var(--text-light);
  }
  .holder-name {
    font-weight: 700; font-size: 17px; letter-spacing: 1px; text-transform: uppercase;
    color: var(--text-muted);
    display: inline-block; padding: 0 6px 3px;
    border-bottom: 2px solid var(--silver);
  }
  .holder-company { font-size: 13px; margin-top: 4px; color: var(--text-light); }
  .contact-lines { margin-top: 48px; font-size: 13.5px; line-height: 1.5; }
  .postal { margin-top: 16px; font-size: 13.5px; }
  /* Logo side */
  .card--brand {
    background: radial-gradient(ellipse at 50% 35%, var(--card-sheen) 0%, #1a1a1a 50%, var(--card-black) 100%);
  }
  .edge-tab {
    position: absolute; width: 22px; height: 38px;
    background: linear-gradient(90deg, var(--silver-dark), #e0e0e0);
  }
  .edge-tab--top-right { right: 0; top: 22px; }
  .edge-tab--bottom-left { left: 0; bottom: 40px; }
  .brand-lockup {
    position: absolute; inset: 0;
    display: flex; align-items: center; justify-content: center; gap: 14px;
  }
  .brand-mark {
    width: 22px; height: 22px; border-radius: 50%; background: var(--silver);
  }
  .brand-name {
    font-weight: 700; font-size: 30px; letter-spacing: 2px; text-transform: uppercase;
    color: var(--silver);
  }
</style>
</head>
<body>
<main class="stage">
  <section class="card card--contact" aria-label="Contact side">
    <div class="edge-band edge-band--left"></div>
    <div class="edge-band edge-band--right"></div>
    <div class="mascot-area" role="img" aria-label="Running stick figure with a magnifying glass head"></div>
    <div class="contact-block">
      <div class="holder-name">Morgan Kilbride</div>
      <div class="holder-company">Brisk Lens Inquiries</div>
      <div class="contact-lines">
        <div class="phone">0438276104</div>
        <div class="email">info@brisklensinquiries.example.au</div>
        <div class="web">www.brisklensinquiries.example.au</div>
      </div>
      <div class="postal">PO Box 58, Fernvale NSW 2291</div>
    </div>
  </section>

  <section class="card card--brand" aria-label="Brand side">
    <div class="edge-tab edge-tab--top-right"></div>
    <div class="edge-tab edge-tab--bottom-left"></div>
    <div class="brand-lockup">
      <span class="brand-name">Brisk Lens Inquiries</span>
      <span class="brand-mark"></span>
    </div>
  </section>
</main>
</body>
</html>
```